ONE PAGE WEB DESIGN NEEDED for Finance Company

We need a web design (ONE PAGE DESIGN ONLY) for a new finance website called Brightwell Lending. Brightwell Lending helps customers get the right loan, whether its a home loan, investment loan, business loan etc.

You are required to come up with just the homepage design. Professionalism and quality is the key factors in the successful design.

Here are a few design questions to help you out:

-
What information should be used on the page?
Ive provided a document which outlines all the information needed to put on homepage (attached to the brief - called brightwell_page_info). Also see the Must Have section below on this brief.

-
What links should appear in the navigation/footer?:
The navigation should provide links to the following pages (NOTE: services link has subcategories):
1 Homepage
2 Services
- Home loans
- Investment loans
- Refinancing loans
- Business loans
3 About Us
4 FAQ
5 Contact Us

-
What colors should be used in the design?
Our company colors - Cyan: #2EADE3, Blue: #004B70, White. Feel free to submit designs with slight variations if you feel it improves the design.

-
What should the layout of the page be?
This is up to you to come up with - we are open to different layouts for the page design (as long as they capture the information effectively and making it easy to understand).

Target Market(s)

Potential Home owners, Families and Business Owners

Industry/Entity Type

Business

Requirements
Must have
• - Must contain our logo (attached as PNG and Illustrator file)
- Winning designer must supply a Photoshop file (PSD) that will allow us.
Nice to have
• - Should include photos/images of families, professional groups, tradespeople etc (you can use stock photos from PixQuarry and I will purchase them once you are selected as the winning design)
- Link to a loan calculator somewhere on front page with a button 'Find out how much you could borrow' (or maybe even try adding a loan calculator to the homepage if you think this would look good)
- Page should have a main headline "Finding the right loan for you" or "Brightwell Lending finds the right loan for our customers."
- Must include Accreditation logos somewhere on the homepage (will try and supply these soon)
Should not have
• - Poor quality designs will not be considered
- Do not use clipart

```html
<!DOCTYPE html>
<html lang="en">
<head>
<meta charset="utf-8">
<title>Brightwell Lending</title>
<link href="https://fonts.googleapis.com/css2?family=Arimo:wght@400;700&family=Josefin+Sans:wght@400&display=swap" rel="stylesheet">
<style>
:root{
  --cyan:#2eade3;
  --blue:#004b70;
  --bar:#6b7283;
  --text:#555;
  --heading:#777;
  --panel:#f3f3f3;
  --line:#cfcfcf;
  --white:#fff;
  --badge-a:#1a5ea8;
  --badge-b:#4a4a4a;
  --badge-c:#2a9a3a;
  --badge-d:#c83a3a;
}
*{margin:0;padding:0;box-sizing:border-box}
html,body{width:1200px;height:1182px;overflow:hidden;background:var(--white);font-family:Arimo,Arial,sans-serif;color:var(--text)}
.page{position:relative;width:1200px;height:1182px}
.topbar{position:absolute;left:0;top:0;width:1200px;height:37px;background:linear-gradient(180deg,#7a8191,var(--bar))}
.social{position:absolute;top:3px;right:57px;display:flex;gap:19px}
.social span{width:30px;height:30px;border-radius:6px;display:block}
.header{position:absolute;left:0;top:37px;width:1200px;height:91px;background:linear-gradient(180deg,#f8f8f8,#e6e6e6)}
.brand{position:absolute;left:52px;top:12px;display:flex;align-items:center;gap:28px}
.brand-mark{width:72px;height:72px;border-radius:50%;border:5px solid var(--cyan)}
.brand-name{font-size:31px;color:var(--cyan);font-weight:400;letter-spacing:-.5px}
.nav{position:absolute;right:43px;top:38px;display:flex;gap:38px;font-size:14px;letter-spacing:1.2px;color:#777}
.nav .active{color:#444;font-weight:700}
.hero{position:absolute;left:0;top:128px;width:1200px;height:245px;background:linear-gradient(180deg,#5ab8e0 0%,#8fd4f0 100%)}
.hero-photo{position:absolute;left:40px;top:2px;width:380px;height:243px;background:linear-gradient(160deg,#c9a37b,#6c8fb0 60%,#a8c7e0)}
.hero-title{position:absolute;left:568px;top:32px;font-family:"Josefin Sans",sans-serif;font-weight:400;font-size:42px;line-height:48px;letter-spacing:2px;color:var(--white)}
.about{position:absolute;left:39px;top:395px;width:832px;height:252px;background:var(--panel);border:1px solid var(--line)}
.about h2{position:absolute;left:23px;top:21px;font-size:25px;font-weight:400;letter-spacing:1.5px;color:#555}
.about-copy{position:absolute;left:20px;top:62px;width:442px;font-size:12.2px;line-height:18px;letter-spacing:.4px;color:#555}
.about-copy p{margin-bottom:18px}
.about-copy p.lead{text-indent:35px}
.about-photo{position:absolute;left:503px;top:24px;width:303px;height:201px;border:1px solid #aaa;background:linear-gradient(135deg,#6f8a5a,#9fb3a0 45%,#3a9ac9 70%,#2d2d2d)}
.calc{position:absolute;left:882px;top:393px;width:279px;height:255px;background:linear-gradient(180deg,#f1f1f1,#e4e4e4);border:1px solid var(--line)}
.calc h3{height:51px;background:linear-gradient(180deg,#8dcdea,#3aa3d6);color:var(--white);font-weight:400;font-size:18px;text-align:center;line-height:52px;letter-spacing:.3px}
.calc-row{position:absolute;left:22px;display:flex;align-items:center;font-size:12.5px;color:#444}
.calc-row label{width:62px}
.calc-field{width:159px;height:27px;border:1px solid #c8c8c8;background:var(--white);border-radius:3px;font-size:12px;color:#999;padding:6px 12px}
.calc-btn{position:absolute;left:84px;top:214px;width:113px;height:34px;border:1px solid #bbb;border-radius:4px;background:linear-gradient(180deg,#fff,#e2e2e2);font-size:11.5px;font-weight:700;color:#444;text-align:center;line-height:33px}
.service{position:absolute;top:686px;width:266px}
.service h4{font-weight:400;font-size:24px;letter-spacing:1px;color:var(--heading);text-align:center;height:38px}
.service-box{height:178px;border:1px solid #ddd;border-radius:8px;background:linear-gradient(180deg,#fdfdfd,#ececec);box-shadow:0 10px 10px -6px rgba(0,0,0,.18);padding:14px 4px 0 16px}
.service li{list-style:none;font-size:14px;letter-spacing:1.1px;line-height:30px;color:#555;padding-left:17px;position:relative;white-space:nowrap}
.service li::before{content:"";position:absolute;left:1px;top:10px;width:6px;height:9px;border-left:2px solid #666;border-top:2px solid #666;transform:skewX(-15deg)}
.service li.plain::before{display:none}
.service li.label{font-weight:700}
.divider{position:absolute;left:75px;top:944px;width:1050px;height:1px;background:#cfcfcf}
.badges{position:absolute;top:965px;left:0;width:1200px;height:106px}
.badge{position:absolute;display:block}
.badge-rect{left:141px;top:15px;width:206px;height:76px;background:var(--badge-a)}
.badge-round{width:100px;height:100px;border-radius:50%;top:3px}
.footer{position:absolute;left:0;top:1090px;width:1200px;height:92px;background:var(--bar)}
.footer-links{position:absolute;left:51px;top:27px;font-size:11.3px;letter-spacing:.6px;color:var(--white)}
.footer-links span{margin:0 7px;color:#d0d3da}
.copyright{position:absolute;left:51px;top:53px;font-size:11.3px;letter-spacing:.6px;color:var(--white)}
</style>
</head>
<body>
<div class="page">
  <div class="topbar">
    <div class="social">
      <span style="background:#3cb6e5"></span>
      <span style="background:#3e68b5"></span>
      <span style="background:#f08a2e"></span>
      <span style="background:#e8e8e8"></span>
    </div>
  </div>

  <header class="header">
    <div class="brand">
      <div class="brand-mark"></div>
      <div class="brand-name">Brightwell Lending</div>
    </div>
    <nav class="nav">
      <span>HOME</span><span class="active">SERVICES</span><span>ABOUT US</span><span>FAQ</span><span>CONTACT US</span>
    </nav>
  </header>

  <section class="hero">
    <div class="hero-photo" role="img" aria-label="Photo of a smiling family with two young children"></div>
    <h1 class="hero-title">WE FIND<br>THE RIGHT LOAN FOR<br>OUR CUSTOMERS</h1>
  </section>

  <section class="about">
    <h2>ABOUT US</h2>
    <div class="about-copy">
      <p class="lead">At Brightwell Lending we work hard to find the right loan for our customers. We do that because we are backed by sound industry knowledge, professional experience and a great customer service approach.</p>
      <p>Brightwell Lending guarantees that we will always tailor the best solution for your individual lending needs.</p>
      <p>We can do that because we have access to a wide variety of lending options from major banks to non-bank lenders and we are committed to finding the right lending product for you.</p>
    </div>
    <div class="about-photo" role="img" aria-label="Photo of a small business owner holding an open sign at a shop door"></div>
  </section>

  <aside class="calc">
    <h3>LOAN CALCULATOR</h3>
    <div class="calc-row" style="top:70px"><label>EMI</label><div class="calc-field"></div></div>
    <div class="calc-row" style="top:120px"><label>RDI</label><div class="calc-field">Enter value in %</div></div>
    <div class="calc-row" style="top:170px"><label>Terms</label><div class="calc-field">Enter value in months</div></div>
    <div class="calc-btn">CALCULATE</div>
  </aside>

  <section class="service" style="left:46px">
    <h4>HOME LOAN</h4>
    <ul class="service-box">
      <li>HOME BUYERS</li>
      <li>FIRST HOME BUYERS</li>
      <li>OVER 20 LENDERS</li>
    </ul>
  </section>
  <section class="service" style="left:326px">
    <h4>INVESTMENT LOAN</h4>
    <ul class="service-box">
      <li>PROPERTY INVESTMENT<br>LOANS</li>
      <li>INTEREST ONLY LOANS</li>
    </ul>
  </section>
  <section class="service" style="left:606px">
    <h4>REFINANCING</h4>
    <ul class="service-box">
      <li>REFINANCING FOR THE BEST<br>RATE</li>
      <li>UPSIZING OR DOWNSIZING</li>
      <li>CHANGE FROM A VARIABLE<br>TO A FIXED RATE</li>
    </ul>
  </section>
  <section class="service" style="left:888px">
    <h4>BUSINESS LOAN</h4>
    <ul class="service-box">
      <li class="plain label">BUSINESS FINANCE</li>
      <li>LONG TERM</li>
      <li>SHORT TERM</li>
      <li>EQUIPMENT AND LEASING</li>
    </ul>
  </section>

  <div class="divider"></div>

  <div class="badges" role="img" aria-label="Accreditation badges">
    <span class="badge badge-rect"></span>
    <span class="badge badge-round" style="left:380px;background:var(--badge-b)"></span>
    <span class="badge badge-round" style="left:501px;background:var(--badge-a)"></span>
    <span class="badge badge-round" style="left:624px;background:var(--badge-b)"></span>
    <span class="badge badge-round" style="left:768px;background:var(--badge-d)"></span>
    <span class="badge badge-round" style="left:914px;background:var(--badge-c)"></span>
  </div>

  <footer class="footer">
    <div class="footer-links">Home<span>|</span>Services<span>|</span>About Us<span>|</span>FAQ<span>|</span>Terms &amp; Conditions<span>|</span>Privacy Policy<span>|</span>Contact Us</div>
    <div class="copyright">Copyright © 2012. brightwelllending.com</div>
  </footer>
</div>
</body>
</html>
```